What's wrong with sitting graphic for Brovatel

Design an info-graphic for posting to Brovatel (correct size for Brovatel) - which explains the health issues with sitting at work. Based on the attached powerpoint mock up. <br/>This can use the image 372816945 from Quillmarrow which I can buy and send to the designer. Or designer can create own image of person sitting at a desk.

Colors

Designer to choose colors to be used in the design.

```html
<!DOCTYPE html>
<html lang="en">
<head>
<meta charset="utf-8">
<title>What's wrong with sitting – Brovatel</title>
<link rel="stylesheet" href="https://fonts.googleapis.com/css2?family=Nunito:wght@700;800;900&display=swap">
<style>
  :root {
    --bg: #c4e8ea;
    --ink: #3d2a86;
    --card: #ffffff;
    --ribbon-start: #6ee6b4;
    --ribbon-end: #7aa8f7;
    --fold: #2f9c86;
    --logo-bg: #1f3180;
    --scene-a: #9dd6d8;
    --scene-b: #8d8fd0;
  }
  * { margin: 0; padding: 0; box-sizing: border-box; }
  html, body { width: 1200px; height: 961px; overflow: hidden; }
  body {
    background: var(--bg);
    font-family: "Nunito", "Arial Rounded MT Bold", sans-serif;
    color: var(--ink);
    position: relative;
  }
  .desk-scene {
    position: absolute;
    left: 66px; top: 300px;
    width: 700px; height: 600px;
    border-radius: 30px;
    background: linear-gradient(160deg, var(--scene-a) 0%, var(--scene-b) 100%);
    opacity: .55;
  }
  .thought {
    position: absolute;
    left: 470px; top: 60px;
    width: 300px; height: 230px;
  }
  .thought svg { position: absolute; inset: 0; overflow: visible; }
  .thought-text {
    position: absolute;
    inset: 0;
    display: flex; align-items: center; justify-content: center;
    text-align: center;
    font-weight: 800;
    font-size: 32px;
    line-height: 1.25;
    padding: 0 30px;
  }
  .card {
    position: absolute;
    left: 849px; width: 288px;
    background: var(--card);
    box-shadow: 0 2px 4px rgba(0,0,0,.08);
  }
  .card--research { top: 74px; height: 406px; }
  .card--answer { top: 524px; height: 261px; }
  .ribbon {
    position: absolute;
    left: -30px;
  }
  .ribbon svg { position: absolute; inset: 0; }
  .ribbon-text {
    position: relative;
    font-weight: 900;
    text-transform: uppercase;
    padding-left: 54px;
  }
  .card--research .ribbon { top: 19px; width: 286px; height: 143px; }
  .card--research .ribbon-text { font-size: 25px; line-height: 28px; padding-top: 8px; }
  .card--answer .ribbon { top: 22px; width: 288px; height: 96px; }
  .card--answer .ribbon-text { font-size: 25px; line-height: 32px; padding-top: 10px; }
  .ribbon-text .highlight { color: #fff; font-size: 29px; }
  .risk-list {
    position: absolute;
    top: 186px; left: 30px;
    list-style: none;
    font-weight: 700;
    font-size: 21px;
    line-height: 30px;
  }
  .risk-list li::before { content: "• "; }
  .answer-body {
    position: absolute;
    top: 160px; left: 30px; right: 20px;
    font-weight: 700;
    font-size: 21px;
    line-height: 29px;
  }
  .brand {
    position: absolute;
    left: 849px; top: 827px;
    width: 288px; height: 66px;
    background: var(--logo-bg);
    color: #fff;
    font-weight: 900;
    font-size: 40px;
    display: flex; align-items: center; justify-content: center;
  }
</style>
</head>
<body>
  <div class="desk-scene" role="img" aria-label="Illustration of a person with glasses sitting at a desk working on a laptop, with books, a pen cup and a mug"></div>

  <div class="thought">
    <svg viewBox="0 0 300 230" aria-hidden="true">
      <ellipse cx="150" cy="110" rx="150" ry="110" fill="#fff" stroke="var(--ink)" stroke-width="4"/>
      <circle cx="48" cy="272" r="14" fill="#fff" stroke="var(--ink)" stroke-width="4"/>
      <circle cx="30" cy="298" r="8" fill="#fff" stroke="var(--ink)" stroke-width="4"/>
    </svg>
    <p class="thought-text">What are the health risks of sitting?</p>
  </div>

  <section class="card card--research">
    <div class="ribbon">
      <svg viewBox="0 0 286 143" preserveAspectRatio="none" aria-hidden="true">
        <defs>
          <linearGradient id="ribbonFill" x1="0" x2="1">
            <stop offset="0" stop-color="var(--ribbon-start)"/>
            <stop offset="1" stop-color="var(--ribbon-end)"/>
          </linearGradient>
        </defs>
        <path d="M30 118 L30 143 L0 118 Z" fill="var(--fold)"/>
        <path d="M0 0 H246 A40 40 0 0 1 286 40 V78 A40 40 0 0 1 246 118 H0 Z" fill="url(#ribbonFill)"/>
      </svg>
      <h2 class="ribbon-text">Research connects excessive sitting with</h2>
    </div>
    <ul class="risk-list">
      <li>Cancer</li>
      <li>Strokes</li>
      <li>Heart attack</li>
      <li>Type 2 diabetes</li>
      <li>Metabolic syndrome</li>
      <li>Premature Death</li>
      <li>Musculoskeletal pain</li>
    </ul>
  </section>

  <section class="card card--answer">
    <div class="ribbon">
      <svg viewBox="0 0 288 96" preserveAspectRatio="none" aria-hidden="true">
        <defs>
          <linearGradient id="ribbonFill2" x1="0" x2="1">
            <stop offset="0" stop-color="var(--ribbon-start)"/>
            <stop offset="1" stop-color="var(--ribbon-end)"/>
          </linearGradient>
        </defs>
        <path d="M30 76 L30 96 L0 76 Z" fill="var(--fold)"/>
        <path d="M0 0 H252 A36 38 0 0 1 288 38 A36 38 0 0 1 252 76 H0 Z" fill="url(#ribbonFill2)"/>
      </svg>
      <h2 class="ribbon-text">The answer?<br><span class="highlight">Get moving</span></h2>
    </div>
    <p class="answer-body">With a standing desk &amp; sit stand coaching software.</p>
  </section>

  <div class="brand">Movelore</div>
</body>
</html>
```